Pet CBD Brand needs a new packaging design*

Dear Designers,<br/><br/>Our brand develops CBD products for animals (dogs & cats) for french speaking customers.<br/><br/>We already have an existing packaging design (see attached files) but would like to freshen the design. The final design should communicate safety & modernity. The design should also clearly express this is a product destined for pets.<br/><br/>We are looking for someone who could redesign the labels of our product line, which includes the following 2 products:<br/>- CBD snacks (250 ml clear jar) label size: 220 x 58 mm<br/>- CBD spray (30 ml clear bottle) label + packaging box.<br/><br/>Please find some important additional aspects:<br/>- We would like to keep our green colors which match our corporate identity (please Google us & visit our website to get a feel for our identity)<br/>**Dark Green RGB(53, 153, 128)<br/>** Light Green RGB(231, 236, 232)<br/><br/>Technical instructions from our printing partner:<br/>- Format: .PDF<br/>- Margins: 2,5 mm<br/>- Colors : CMYK<br/>- All text must be vectorized<br/>- Printing standard: ISOcoated V2<br/>- Minimum resolutions: 300 dpi for images, 1,200 dpi for graphics
Target Market(s)
Pet owners, CBD shops, veterinary clinics
Industry/Entity Type
Alternative Medicine

```html
<!DOCTYPE html>
<html lang="fr">
<head>
<meta charset="utf-8">
<title>Verdalis – gamme CBD pour chiens et chats</title>
<link rel="stylesheet" href="https://fonts.googleapis.com/css2?family=Nunito:wght@800;900&family=Quicksand:wght@400;500;600&display=swap">
<style>
  :root {
    --green: #3aa586;
    --green-tint: #dcefe8;
    --light-green: #e7ece8;
    --ink: #1c2a23;
    --white: #ffffff;
    --label-grey: #f4f5f4;
    --bg-top: #dcdcdb;
    --bg-bottom: #ffffff;
  }
  * { box-sizing: border-box; margin: 0; padding: 0; }
  html, body { width: 1200px; height: 800px; overflow: hidden; }
  body {
    position: relative;
    background: linear-gradient(180deg, var(--bg-top) 0%, #efefee 45%, var(--bg-bottom) 85%);
    font-family: "Quicksand", sans-serif;
    color: var(--ink);
  }
  .panel { position: absolute; background: var(--white); }
  .spine { position: absolute; background: var(--green); }

  .brand {
    position: absolute; left: 0; right: 0;
    display: flex; flex-direction: column; align-items: center;
  }
  .brand-dot { border-radius: 50%; background: var(--green); }
  .brand-name { font-family: "Quicksand", sans-serif; font-weight: 600; color: var(--ink); letter-spacing: .04em; line-height: 1; }

  .product-title {
    position: absolute; left: 0; right: 0; text-align: center;
    font-family: "Nunito", sans-serif; font-weight: 900; color: var(--green); line-height: 1;
  }
  .product-sub {
    position: absolute; left: 0; right: 0; text-align: center;
    font-weight: 500; color: var(--ink); letter-spacing: .02em; line-height: 1;
  }
  .range-name {
    position: absolute; writing-mode: vertical-rl; transform: rotate(180deg);
    font-weight: 400; color: var(--ink); letter-spacing: .03em; line-height: 1;
  }
  .thc {
    position: absolute; display: flex; align-items: center; justify-content: center;
  }
  .thc svg { position: absolute; inset: 0; }
  .thc span {
    position: relative; font-family: "Nunito", sans-serif; font-weight: 900;
    color: var(--ink); text-align: center; line-height: .9;
  }
  .pets-art {
    position: absolute; border-radius: 40% 40% 8px 8px; background: linear-gradient(180deg, var(--green-tint), #eef7f3);
  }
  .net {
    position: absolute; left: 0; right: 0; text-align: center; color: var(--green); font-weight: 500; line-height: 1;
  }

  /* Snacks box */
  .snacks-box { left: 158px; top: 278px; width: 260px; height: 382px; }
  .snacks-box-spine { left: 113px; top: 296px; width: 45px; height: 364px; }

  /* Jar label */
  .jar-label { left: 433px; top: 412px; width: 269px; height: 196px; background: var(--label-grey); }

  /* Spray box */
  .spray-box { left: 725px; top: 305px; width: 91px; height: 378px; }
  .spray-box-side { left: 816px; top: 305px; width: 60px; height: 378px; padding: 100px 4px 0 5px; }
  .usage { color: var(--white); font-size: 5.6px; line-height: 1.45; font-weight: 500; }
  .usage-title { font-weight: 600; margin-bottom: 2px; font-size: 6px; }
  .batch { position: absolute; left: 5px; right: 4px; top: 292px; color: var(--white); font-size: 5px; line-height: 1.5; }

  /* Bottle label */
  .bottle-label { left: 872px; top: 487px; width: 111px; height: 166px; background: var(--label-grey); }
</style>
</head>
<body>

  <!-- Snacks box -->
  <div class="spine snacks-box-spine"></div>
  <section class="panel snacks-box">
    <div class="brand" style="top:34px;gap:6px">
      <span class="brand-dot" style="width:14px;height:14px"></span>
      <span class="brand-name" style="font-size:19px">VERDALIS</span>
    </div>
    <div class="range-name" style="left:16px;top:114px;height:180px;font-size:26px">VERDACROC</div>
    <div class="product-title" style="top:114px;left:60px;right:0;text-align:left;font-size:29px">Snacks CBD</div>
    <div class="product-sub" style="top:157px;left:70px;right:0;text-align:left;font-size:13.5px">POUR CHIENS &amp; CHATS</div>
    <div class="thc" style="left:198px;top:184px;width:44px;height:44px">
      <svg viewBox="0 0 44 44"><polygon points="12,3 32,3 42,22 32,41 12,41 2,22" fill="none" stroke="#1c2a23" stroke-width="1.6"/></svg>
      <span style="font-size:10px">0%<br>THC</span>
    </div>
    <div class="pets-art" role="img" aria-label="Silhouette au trait d'un chien et d'un chat assis côte à côte" style="left:88px;top:214px;width:86px;height:114px"></div>
    <div class="net" style="top:346px;font-size:17px">250g</div>
  </section>

  <!-- Jar label -->
  <section class="panel jar-label">
    <div class="range-name" style="left:20px;top:26px;height:144px;font-size:18px">VERDACROC</div>
    <div class="brand" style="top:16px;gap:5px">
      <span class="brand-dot" style="width:11px;height:11px"></span>
      <span class="brand-name" style="font-size:14px">VERDALIS</span>
    </div>
    <div class="product-title" style="top:64px;font-size:22px">Snacks CBD</div>
    <div class="product-sub" style="top:92px;font-size:10.5px">POUR CHIENS &amp; CHATS</div>
    <div class="thc" style="left:215px;top:100px;width:36px;height:36px">
      <svg viewBox="0 0 36 36"><polygon points="10,2 26,2 34,18 26,34 10,34 2,18" fill="none" stroke="#1c2a23" stroke-width="1.4"/></svg>
      <span style="font-size:8.5px">0%<br>THC</span>
    </div>
    <div class="pets-art" role="img" aria-label="Silhouette au trait d'un chien et d'un chat assis" style="left:110px;top:110px;width:50px;height:60px"></div>
    <div class="net" style="top:176px;font-size:14px">250g</div>
  </section>

  <!-- Spray box -->
  <section class="panel spray-box">
    <div class="brand" style="top:28px;gap:4px">
      <span class="brand-dot" style="width:9px;height:9px"></span>
      <span class="brand-name" style="font-size:9.5px">VERDALIS</span>
    </div>
    <div class="product-title" style="top:88px;font-size:16px">Spray CBD</div>
    <div class="product-sub" style="top:112px;font-size:7.4px">POUR CHIENS &amp; CHATS</div>
    <div class="range-name" style="left:8px;top:150px;height:110px;font-size:15px">VERDASOIN</div>
    <div class="thc" style="left:57px;top:152px;width:25px;height:25px">
      <svg viewBox="0 0 25 25"><polygon points="7,1.5 18,1.5 23.5,12.5 18,23.5 7,23.5 1.5,12.5" fill="none" stroke="#1c2a23" stroke-width="1.1"/></svg>
      <span style="font-size:6px">0%<br>THC</span>
    </div>
    <div class="pets-art" role="img" aria-label="Silhouette au trait d'un chien et d'un chat assis" style="left:22px;top:262px;width:46px;height:68px"></div>
    <div class="net" style="top:348px;font-size:9px">30ml</div>
  </section>
  <aside class="spine spray-box-side">
    <div class="usage">
      <p class="usage-title">Conseil d'utilisation:</p>
      <p>Vaporiser deux fois dans la gueule de l'animal, matin et soir. Adapter la dose selon le poids. Bien agiter avant emploi. Conserver à l'abri de la lumière et de la chaleur. Tenir hors de portée des enfants. Ne pas dépasser la dose conseillée. Demander l'avis du vétérinaire.</p>
    </div>
    <p class="batch">Lot 300044 CBD<br>Fabriqué en France</p>
  </aside>

  <!-- Bottle label -->
  <section class="panel bottle-label">
    <div class="brand" style="top:12px;gap:3px">
      <span class="brand-dot" style="width:8px;height:8px"></span>
      <span class="brand-name" style="font-size:8.5px">VERDALIS</span>
    </div>
    <div class="range-name" style="left:6px;top:50px;height:86px;font-size:9px">VERDASOIN</div>
    <div class="product-title" style="top:52px;left:16px;font-size:15px">Spray CBD</div>
    <div class="product-sub" style="top:74px;left:16px;font-size:7px">POUR CHIENS &amp; CHATS</div>
    <div class="thc" style="left:80px;top:92px;width:21px;height:21px">
      <svg viewBox="0 0 21 21"><polygon points="6,1.2 15,1.2 19.8,10.5 15,19.8 6,19.8 1.2,10.5" fill="none" stroke="#1c2a23" stroke-width="1"/></svg>
      <span style="font-size:5px">0%<br>THC</span>
    </div>
    <div class="pets-art" role="img" aria-label="Silhouette au trait d'un chien et d'un chat assis" style="left:42px;top:104px;width:34px;height:38px"></div>
    <div class="net" style="top:150px;font-size:8px">30ml</div>
  </section>

</body>
</html>
```